Website redesign for Ka-Strata, a leading semiconductor design company

I have an existing website design created in Figma, but I am looking for a completely new and more professional design with a stronger user experience (UX) and modern visual style. The new design should maintain the same text content, not exact text, page purposes, and sections, but the entire UI should be redesigned from scratch. The website should be fully coded and developed. The website is about 10 pages in total.
Scope of Work
1. UI/UX Redesign
Create new, modern, and professional designs for all pages.

Use the existing Figma file ONLY for but we are open for new and innovative ideas:
Text content Not exact text
Propose professional and catchy text
Page purposes
Sections
Visual design must be fully new, not a modification of the current layout.
Primary color palette: Blue & White
You are free to add complementary colors to improve aesthetics and usability.

Design must follow best practices for:
User experience
Visual hierarchy
Accessibility
Readability

2. Responsive Design
The entire website must be designed and developed to work perfectly on:
Desktop (all screen sizes)
Tablets (portrait & landscape)
Mobile Phones (all screen sizes)
Responsive layouts must be customized, not simply scaled.

3. Website Development
Convert the final approved design into a fully functional website.
Clean, modern, and maintainable code.
Technologies HTML/CSS/Javascript - Native design not using platforms such as wordpress
Fast-loading pages, SEO-friendly structure.
Content API Structured
AI-Optimized Content Layout
Functionality such as form submission (contact us) or email composing (careers)
Integrate any needed animations or interactions.
Ensure cross-browser compatibility.
Deliverables
Fully redesigned UI for all pages (in Figma or similar).
Fully responsive front-end development.
Deployment-ready codebase.
Source files for both design and code.

Files to be shared
Current design files (png/pdf format)
Current figma design
Pages structure
Pages content

```html
<!DOCTYPE html>
<html lang="en">
<head>
<meta charset="utf-8">
<title>Ka-Strata — AI-Augmented Silicon</title>
<link rel="stylesheet" href="https://fonts.googleapis.com/css2?family=Exo+2:wght@600;700&family=Inter:wght@400;500;600;700&display=swap">
<style>
:root{
  --navy:#0f2342;
  --navy-deep:#0c1c36;
  --cyan:#00e1f5;
  --ink:#0f1b2e;
  --muted:#6b7689;
  --line:#e6eaf0;
  --soft:#f3f6fb;
  --white:#ffffff;
  --star:#f5b400;
}
*{box-sizing:border-box;margin:0;padding:0}
html,body{width:1200px;height:5047px;overflow:hidden}
body{font-family:"Inter",sans-serif;color:var(--ink);background:var(--white);position:relative}
.abs{position:absolute}
h1,h2,h3.display{font-family:"Exo 2",sans-serif;font-weight:700}
.eyebrow{font-size:12px;font-weight:600;letter-spacing:1.5px;text-transform:uppercase;color:var(--muted)}
.btn{display:inline-flex;align-items:center;justify-content:center;height:46px;padding:0 26px;border-radius:23px;font-size:14px;font-weight:600;background:var(--cyan);color:var(--navy);text-decoration:none}
.btn-ghost{background:transparent;border:2px solid #fff;color:#fff}
.btn-dark{background:var(--navy);color:#fff}

/* nav */
.nav{left:0;top:0;width:1200px;height:84px;background:var(--navy);z-index:5}
.brand{font-family:"Exo 2",sans-serif;font-weight:700;font-size:24px;color:#fff}
.nav .brand{left:55px;top:26px}
.nav-links{left:372px;top:34px;display:flex;gap:26px;font-size:14px;color:#fff;font-weight:500}
.nav .btn{right:57px;top:19px;height:46px;padding:0 26px}

/* hero */
.hero{left:0;top:84px;width:1200px;height:638px;background:linear-gradient(120deg,#3a4b5e 0%,#4d5e70 40%,#5c6a78 70%,#46525f 100%)}
.hero-shade{inset:0;background:rgba(22,34,56,.55)}
.hero .eyebrow{left:294px;top:132px;color:var(--cyan)}
.hero h1{left:294px;top:162px;font-size:52px;line-height:60px;color:#fff;width:640px}
.hero p{left:294px;top:304px;width:600px;font-size:16px;line-height:26px;color:#eef2f8}
.hero .btn.primary{left:296px;top:384px;height:48px}
.hero .btn-ghost{left:488px;top:384px;height:48px}

.feature{top:667px;width:343px;height:102px;background:#fff;border-radius:4px;box-shadow:0 10px 30px rgba(15,35,66,.12);display:flex;align-items:center;gap:18px;padding:0 22px}
.feature svg{flex:none}
.feature b{display:block;font-size:15px;font-weight:600}
.feature span{font-size:13px;color:var(--muted)}

/* about */
.about-img{left:57px;top:902px;width:412px;height:396px;background:linear-gradient(135deg,#8fc1e8,#3f7fc4 60%,#1f3d7a);border-radius:4px}
.about-img2{left:318px;top:1186px;width:249px;height:179px;background:linear-gradient(135deg,#3a4438,#1e2622);border:6px solid #fff;border-radius:4px}
.about-text{left:628px;top:928px;width:515px}
.about-text h2{font-size:34px;line-height:54px;margin:14px 0 14px}
.about-text p{font-size:15px;line-height:25px;color:var(--muted)}
.checks{list-style:none;margin:20px 0 24px}
.checks li{display:flex;align-items:center;gap:12px;font-size:15px;font-weight:500;height:35px}

/* capabilities */
.caps{left:0;top:1445px;width:1200px;height:630px;background:var(--soft)}
.center{width:1200px;text-align:center}
.caps .eyebrow{top:78px}
.caps h2{top:106px;font-size:34px}
.cap{top:188px;width:343px;height:369px;background:#fff;border-radius:4px;box-shadow:0 4px 16px rgba(15,35,66,.06);overflow:hidden}
.cap .ph{height:228px;position:relative}
.cap .ic{position:absolute;left:20px;bottom:-6px;width:54px;height:54px;background:#fff;border-radius:4px;display:flex;align-items:center;justify-content:center}
.cap h3{font-size:18px;font-weight:600;margin:22px 22px 12px}
.cap p{font-size:13px;line-height:22px;color:var(--muted);margin:0 22px}

/* gallery */
.gallery .eyebrow{left:57px;top:2157px}
.gallery h2{left:57px;top:2176px;font-size:34px}
.gallery p.lead{left:600px;top:2154px;width:540px;font-size:15px;line-height:25px;color:var(--ink)}
.gallery .btn{left:600px;top:2218px}
.tile{border-radius:4px;overflow:hidden}
.tile .cap-t{position:absolute;left:18px;bottom:18px;color:#fff}
.tile .cap-t b{display:block;font-size:18px;font-weight:600;margin-bottom:12px}
.tile .cap-t span{font-size:12px;color:var(--cyan)}

/* band */
.band{left:0;top:2942px;width:1200px;height:160px;background:var(--navy)}
.band h2{left:57px;top:62px;font-size:30px;color:#fff}
.band .btn{right:57px;top:56px}

/* reviews */
.reviews .eyebrow{top:3180px}
.reviews h2{top:3208px;font-size:34px}
.review{top:3291px;width:343px;height:223px;border:1px solid var(--line);border-radius:4px;padding:28px 28px}
.stars{color:var(--star);font-size:16px;letter-spacing:3px}
.review q{display:block;font-style:italic;font-size:14px;line-height:23px;margin:12px 0 18px;quotes:"\201C" "\201D"}
.who{display:flex;align-items:center;gap:16px}
.avatar{width:46px;height:46px;border-radius:50%;background:#c9d3df}
.who b{display:block;font-size:15px;font-weight:600}
.who span{font-size:12px;color:var(--muted)}

/* expertise */
.expertise{left:0;top:3593px;width:1200px;height:525px;background:var(--soft)}
.expertise .eyebrow{left:57px;top:112px}
.expertise h2{left:57px;top:132px;font-size:34px;line-height:54px;width:500px}
.expertise p{left:57px;top:248px;width:520px;font-size:15px;line-height:25px;color:var(--muted)}
.stat{top:350px}
.stat b{display:block;font-family:"Exo 2",sans-serif;font-size:44px;font-weight:600}
.stat span{font-size:12px;font-weight:600;letter-spacing:.5px;color:var(--muted)}
.exp-img{left:628px;top:72px;width:515px;height:375px;background:linear-gradient(135deg,#8b6a4c,#4d4136 55%,#2d2a28);border-radius:4px}
.trust{left:600px;top:306px;width:151px;height:112px;background:var(--cyan);padding:20px 28px;color:var(--navy)}
.trust span{font-size:12px;display:block}
.trust b{font-family:"Exo 2",sans-serif;font-size:30px;display:block;line-height:36px}

/* why */
.why .eyebrow{left:57px;top:4196px}
.why h2{left:57px;top:4218px;font-size:34px}
.why p{left:57px;top:4290px;width:400px;font-size:15px;line-height:25px;color:var(--muted)}
.why-card{width:298px;height:130px;border:1px solid var(--line);border-radius:4px;padding:22px 20px;background:#fff}
.why-card h3{font-size:16px;font-weight:600;margin:14px 0 12px}
.why-card span{font-size:12px;color:var(--muted)}

/* footer */
.footer{left:0;top:4667px;width:1200px;height:380px;background:var(--navy-deep);color:#fff}
.cta{left:57px;top:4557px;width:1086px;height:165px;background:var(--cyan);border-radius:4px;z-index:2}
.cta h2{position:absolute;left:46px;top:54px;font-size:30px;color:var(--navy)}
.cta p{position:absolute;left:46px;top:100px;font-size:14px;color:var(--navy)}
.cta .btn{position:absolute;right:46px;top:60px}
.fcol h4{font-size:15px;font-weight:600;margin-bottom:20px}
.fcol a{display:block;font-size:13px;color:#c9d2e0;text-decoration:none;margin-bottom:17px}
.fabout{left:57px;top:4770px;width:270px}
.fabout p{font-size:13px;line-height:21px;color:#c9d2e0;margin-top:22px}
.contact-row{display:flex;align-items:center;gap:8px;font-size:14px;color:#fff;margin-bottom:16px}
.fline{left:57px;top:4975px;width:1086px;height:1px;background:rgba(255,255,255,.12)}
.copy{top:5000px;font-size:12px;color:#9aa6ba}
</style>
</head>
<body>

<header class="nav abs">
  <div class="brand abs">Ka-Strata</div>
  <nav class="nav-links abs"><span>Solutions</span><span>Verification</span><span>Industries</span><span>Academy</span><span>Careers</span></nav>
  <a class="btn abs">Contact Us</a>
</header>

<section class="hero abs" role="img" aria-label="Electronics workbench with circuit boards, sensors and breadboards">
  <div class="hero-shade abs"></div>
  <div class="eyebrow abs">Building your dreams to reality</div>
  <h1 class="abs">Powering the Future with AI-Augmented Silicon</h1>
  <p class="abs">End-to-end IP development and ISO-certified semiconductor solutions for the AI, HPC, and Automotive eras.</p>
  <a class="btn primary abs">Explore Solutions</a>
  <a class="btn btn-ghost abs">Ka-Strata Academy</a>
</section>

<div class="feature abs" style="left:57px">
  <svg width="30" height="30" viewBox="0 0 30 30" fill="none" stroke="#0f1b2e" stroke-width="2"><rect x="8" y="8" width="14" height="14" rx="1"/><rect x="12" y="12" width="6" height="6" fill="#0f1b2e"/><path d="M11 3v5M15 3v5M19 3v5M11 22v5M15 22v5M19 22v5M3 11h5M3 15h5M3 19h5M22 11h5M22 15h5M22 19h5"/></svg>
  <div><b>Silicon-Proven IP</b><span>High-performance reliable designs.</span></div>
</div>
<div class="feature abs" style="left:428px">
  <svg width="30" height="30" viewBox="0 0 30 30"><path d="M15 3l10 4v7c0 7-4.5 11-10 13C9.5 25 5 21 5 14V7z" fill="none" stroke="#0f1b2e" stroke-width="2.4"/><path d="M15 5v20c4-2 8-5 8-11V8z" fill="#0f1b2e"/></svg>
  <div><b>ISO 26262 Certified</b><span>Safety-critical automotive compliance.</span></div>
</div>
<div class="feature abs" style="left:800px">
  <svg width="30" height="30" viewBox="0 0 30 30" fill="#0f1b2e"><path d="M14 4c-4 0-6 2-6 5-3 1-4 4-3 7-1 3 1 7 5 7 1 2 2 3 4 3z"/><path d="M16 4c4 0 6 2 6 5 3 1 4 4 3 7 1 3-1 7-5 7-1 2-2 3-4 3z"/></svg>
  <div><b>AI-Driven Design</b><span>Augmented verification flows.</span></div>
</div>

<!-- about -->
<div class="about-img abs" role="img" aria-label="Engineer in a cleanroom suit inspecting a silicon wafer"></div>
<div class="about-img2 abs" role="img" aria-label="Close-up of a printed circuit board"></div>
<div class="about-text abs">
  <div class="eyebrow">Trusted innovation partner</div>
  <h2>Semiconductor Excellence in Every Circuit.</h2>
  <p>Ka-Strata delivers high-quality verification and reliable designs that meet global standards. From Data Centers to Healthcare, we turn concepts into silicon reality.</p>
  <ul class="checks">
    <li><svg width="14" height="14" viewBox="0 0 14 14"><path d="M2 7l3.5 3.5L12 3" fill="none" stroke="#00c8dc" stroke-width="2"/></svg>End-to-End IP Development</li>
    <li><svg width="14" height="14" viewBox="0 0 14 14"><path d="M2 7l3.5 3.5L12 3" fill="none" stroke="#00c8dc" stroke-width="2"/></svg>Pre-Silicon Verification</li>
    <li><svg width="14" height="14" viewBox="0 0 14 14"><path d="M2 7l3.5 3.5L12 3" fill="none" stroke="#00c8dc" stroke-width="2"/></svg>Staffing &amp; Academy Training</li>
  </ul>
  <a class="btn">Learn More</a>
</div>

<!-- capabilities -->
<section class="caps abs">
  <div class="eyebrow abs center">Our capabilities</div>
  <h2 class="abs center">Full-Spectrum Chip Services</h2>
  <article class="cap abs" style="left:57px">
    <div class="ph" role="img" aria-label="Engineer working at a computer in a dark lab" style="background:linear-gradient(135deg,#3b2a6e,#15122e)"><div class="ic"><svg width="22" height="22" viewBox="0 0 22 22" fill="#0f1b2e"><path d="M11 2l9 4-9 4-9-4z"/><path d="M2 10l9 4 9-4v2l-9 4-9-4zM2 14l9 4 9-4v2l-9 4-9-4z"/></svg></div></div>
    <h3>IP Development</h3><p>Custom analog and digital IP blocks designed for high performance and low power consumption.</p>
  </article>
  <article class="cap abs" style="left:428px">
    <div class="ph" role="img" aria-label="Team reviewing verification results on laptops" style="background:linear-gradient(135deg,#6a5040,#2c2624)"><div class="ic"><svg width="22" height="22" viewBox="0 0 22 22" fill="none" stroke="#0f1b2e" stroke-width="2.4"><circle cx="9" cy="9" r="6"/><path d="M14 14l6 6"/></svg></div></div>
    <h3>Verification &amp; Testing</h3><p>Rigorous pre-silicon verification methodologies to ensure zero-bug tape-outs.</p>
  </article>
  <article class="cap abs" style="left:800px">
    <div class="ph" role="img" aria-label="Students collaborating in a training session" style="background:linear-gradient(135deg,#6a5040,#2c2624)"><div class="ic"><svg width="24" height="22" viewBox="0 0 24 22" fill="#0f1b2e"><path d="M12 3L1 8l11 5 11-5z"/><path d="M5 11v5c3 3 11 3 14 0v-5l-7 3z"/></svg></div></div>
    <h3>Ka-Strata Academy</h3><p>Professional training programs to build the next generation of chip architects and engineers.</p>
  </article>
</section>

<!-- gallery -->
<section class="gallery">
  <div class="eyebrow abs">Built to last</div>
  <h2 class="abs">Designed to Inspire.</h2>
  <p class="lead abs">Every design we ship balances performance, power and safety, engineered to meet the demands of tomorrow's most critical systems.</p>
  <a class="btn abs">View Case Studies</a>
  <div class="tile abs" role="img" aria-label="Sports car on an empty road under a cloudy sky" style="left:57px;top:2304px;width:639px;height:485px;background:linear-gradient(180deg,#c9ccd0 0%,#8a8e93 55%,#4b4f55 100%)">
    <div class="cap-t"><b>Automotive ADAS</b><span>ISO 26262 Compliant</span></div></div>
  <div class="tile abs" role="img" aria-label="Data center aisle lit in blue" style="left:716px;top:2304px;width:427px;height:232px;background:linear-gradient(135deg,#3757c9,#1a246a 60%,#0c1240)">
    <div class="cap-t"><b>HPC Data Centers</b><span>High Speed Interconnects</span></div></div>
  <div class="tile abs" role="img" aria-label="Doctor holding a smartphone with stethoscope" style="left:716px;top:2557px;width:427px;height:232px;background:linear-gradient(135deg,#d9dde2,#9aa4ae 60%,#3c4650)">
    <div class="cap-t"><b>Smart Healthcare</b><span>Low Power Biosensors</span></div></div>
</section>

<section class="band abs">
  <h2 class="abs">Accelerating Innovation from Architecture to Tape-out.</h2>
  <a class="btn abs">Get a Quote</a>
</section>

<!-- reviews -->
<section class="reviews">
  <div class="eyebrow abs center">Reviews</div>
  <h2 class="abs center">What Our Clients Say</h2>
  <article class="review abs" style="left:57px"><div class="stars">★★★★★</div><q>Ka-Strata's verification process saved us months of development time. Their team is world-class.</q><div class="who"><div class="avatar"></div><div><b>Daniel Corvell</b><span>CTO, Drivelane Systems</span></div></div></article>
  <article class="review abs" style="left:428px"><div class="stars">★★★★★</div><q>The IP Cores provided were rock solid and extremely power efficient for our IoT devices.</q><div class="who"><div class="avatar"></div><div><b>Sara Lindqvist</b><span>Lead Architect, Nanoforge Labs</span></div></div></article>
  <article class="review abs" style="left:800px"><div class="stars">★★★★★</div><q>Ka-Strata Academy graduates were ready to work on day one. A great talent ecosystem.</q><div class="who"><div class="avatar"></div><div><b>Marcus Ortega</b><span>HR Director, Gridwell Semi</span></div></div></article>
</section>

<!-- expertise -->
<section class="expertise abs">
  <div class="eyebrow abs">Our expertise</div>
  <h2 class="abs">Backed by Results, Built on Relationships.</h2>
  <p class="abs">We combine human ingenuity with AI augmentation to solve the hardest problems in physics and logic.</p>
  <div class="stat abs" style="left:57px"><b>100+</b><span>IPS DELIVERED</span></div>
  <div class="stat abs" style="left:204px"><b>15+</b><span>YEARS EXPERIENCE</span></div>
  <div class="exp-img abs" role="img" aria-label="Engineers collaborating around laptops at a wooden table"></div>
  <div class="trust abs"><span>Trusted by</span><b>50+</b><span>Global Partners</span></div>
</section>

<!-- why -->
<section class="why">
  <div class="eyebrow abs">Why choose us</div>
  <h2 class="abs">What Sets Us Apart</h2>
  <p class="abs">We don't just design chips; we architect the future with precision, speed, and reliability.</p>
  <div class="why-card abs" style="left:520px;top:4191px"><svg width="20" height="20" viewBox="0 0 20 20" fill="#0f1b2e"><path d="M18 2c-6 0-10 3-12 8l4 4c5-2 8-6 8-12zM5 11l-3 1 2 2zM9 15l-1 3 2-2z"/><circle cx="13" cy="7" r="1.6" fill="#fff"/></svg><h3>Fast Time-to-Market</h3><span>Accelerated flows using AI tools.</span></div>
  <div class="why-card abs" style="left:845px;top:4191px"><svg width="20" height="20" viewBox="0 0 20 20" fill="none" stroke="#0f1b2e" stroke-width="2"><circle cx="10" cy="10" r="8"/><path d="M2 10h16M10 2c3 3 3 13 0 16M10 2c-3 3-3 13 0 16"/></svg><h3>Global Compliance</h3><span>Meeting ISO &amp; intl. standards.</span></div>
  <div class="why-card abs" style="left:520px;top:4351px"><svg width="22" height="20" viewBox="0 0 22 20" fill="#0f1b2e"><rect x="3" y="2" width="16" height="9" rx="2"/><circle cx="11" cy="14" r="3"/><rect x="2" y="16" width="18" height="3" rx="1"/></svg><h3>Talent Ecosystem</h3><span>Continuous pipeline of engineers.</span></div>
  <div class="why-card abs" style="left:845px;top:4351px"><svg width="24" height="20" viewBox="0 0 24 20" fill="#0f1b2e"><path d="M1 5h5l6 5-3 3-4-3H1zM23 5h-5l-7 6 2 2 3-2h7z"/></svg><h3>Long-Term Support</h3><span>Post-silicon validation support.</span></div>
</section>

<footer class="footer abs"></footer>
<div class="cta abs">
  <h2>Your Vision. Our Reality.</h2>
  <p>Let's begin your next semiconductor project.</p>
  <a class="btn btn-dark">Contact Us</a>
</div>
<div class="fcol fabout abs"><div class="brand" style="font-size:20px">Ka-Strata</div><p>AI-augmented semiconductor innovation partner delivering end-to-end IP development and verification.</p></div>
<div class="fcol abs" style="left:418px;top:4766px;color:#fff"><h4>Services</h4><a>IP Development</a><a>Verification</a><a>Consulting</a><a>Academy</a></div>
<div class="fcol abs" style="left:673px;top:4766px;color:#fff"><h4>Company</h4><a>About Us</a><a>Careers</a><a>Blog</a><a>Contact</a></div>
<div class="fcol abs" style="left:928px;top:4766px;color:#fff"><h4>Contact</h4>
  <div class="contact-row"><svg width="12" height="14" viewBox="0 0 12 14" fill="#fff"><path d="M6 0a5 5 0 015 5c0 4-5 9-5 9S1 9 1 5a5 5 0 015-5z"/><circle cx="6" cy="5" r="2" fill="#0c1c36"/></svg>Silicon Valley, CA</div>
  <div class="contact-row"><svg width="14" height="11" viewBox="0 0 14 11" fill="#fff"><rect width="14" height="11" rx="1"/><path d="M0 1l7 5 7-5" fill="none" stroke="#0c1c36" stroke-width="1.4"/></svg>hello@ka-strata.example</div>
  <div class="contact-row"><svg width="13" height="13" viewBox="0 0 13 13" fill="#fff"><path d="M3 0l2 3-1.5 1.5c1 2 3 4 5 5L10 8l3 2-1 3C6 13 0 7 0 1z"/></svg>+1 (555) 010-2468</div>
</div>
<div class="fline abs"></div>
<div class="copy abs center">© 2024 Ka-Strata. All rights reserved.</div>

</body>
</html>
```